Create a professional, eye-catching business card design that reflects the values and services of Brookfern Veterinary Hospital. we provide veterinary services and the business card should be a memorable representation of the clinic and align with its branding and mission. our tag line is "Life Long Companions, Lifelong Care"
Use clean, modern typography. Prioritize readability and professionalism. We would like to see designs that use the color blue, as in the logo example. the final design should communicate professionalism and care, with attention to detail.

```html
<!DOCTYPE html>
<html lang="en">
<head>
<meta charset="utf-8">
<title>Brookfern Veterinary Hospital — Business Card</title>
<link href="https://fonts.googleapis.com/css2?family=Montserrat:wght@400;500;700;800&display=swap" rel="stylesheet">
<style>
  :root {
    --navy: #1c3160;
    --white: #ffffff;
    --backdrop: #8a8a8a;
    --shadow: rgba(0, 0, 0, 0.35);
  }
  * { box-sizing: border-box; margin: 0; padding: 0; }
  html, body {
    width: 1200px;
    height: 1200px;
    overflow: hidden;
    background: var(--backdrop);
    font-family: "Montserrat", Arial, sans-serif;
  }
  .card {
    position: absolute;
    width: 885px;
    height: 517px;
    left: 157px;
    box-shadow: 4px 6px 10px var(--shadow);
    overflow: hidden;
  }
  .card-front { top: 59px; background: var(--white); display: flex; }
  .card-back { top: 622px; background: var(--navy); display: flex; align-items: center; justify-content: center; }

  .brand {
    display: flex;
    flex-direction: column;
    align-items: center;
    font-weight: 800;
    text-transform: uppercase;
    line-height: 1;
  }
  .brand-mark {
    width: 150px;
    height: 150px;
    border: 3px solid currentColor;
    border-radius: 50%;
    margin-bottom: 22px;
  }
  .brand-name { font-size: 46px; letter-spacing: 1px; }
  .brand-sub { font-size: 19px; margin-top: 6px; letter-spacing: 0.3px; }

  .front-brand-area {
    width: 428px;
    height: 100%;
    display: flex;
    align-items: center;
    justify-content: center;
    color: var(--navy);
    padding-bottom: 20px;
  }
  .card-back .brand { color: var(--white); padding-top: 18px; }

  .contact-panel {
    width: 457px;
    height: 100%;
    background: var(--navy);
    padding: 70px 0 69px;
    display: flex;
    flex-direction: column;
    justify-content: space-between;
  }
  .contact-row {
    height: 71px;
    background: var(--white);
    display: flex;
    align-items: center;
    color: var(--navy);
    font-size: 22px;
    font-weight: 500;
  }
  .contact-icon {
    width: 30px;
    height: 30px;
    margin-left: 52px;
    margin-right: 46px;
    flex: none;
    fill: var(--navy);
  }
  .contact-row.web { font-weight: 700; }
  .contact-row.address { line-height: 1.25; font-size: 21px; }
</style>
</head>
<body>
  <section class="card card-front">
    <div class="front-brand-area">
      <div class="brand">
        <div class="brand-mark"></div>
        <span class="brand-name">Brookfern</span>
        <span class="brand-sub">Veterinary Hospital</span>
      </div>
    </div>
    <div class="contact-panel">
      <div class="contact-row phone">
        <svg class="contact-icon" viewBox="0 0 24 24" aria-hidden="true"><path d="M6.6 10.8a15.1 15.1 0 0 0 6.6 6.6l2.2-2.2a1 1 0 0 1 1-.25 11.4 11.4 0 0 0 3.6.57 1 1 0 0 1 1 1V20a1 1 0 0 1-1 1A17 17 0 0 1 3 4a1 1 0 0 1 1-1h3.5a1 1 0 0 1 1 1c0 1.25.2 2.45.57 3.57a1 1 0 0 1-.25 1z"/></svg>
        <span>1234 567 890</span>
      </div>
      <div class="contact-row email">
        <svg class="contact-icon" viewBox="0 0 24 24" aria-hidden="true"><path d="M3 5h18a1 1 0 0 1 1 1v12a1 1 0 0 1-1 1H3a1 1 0 0 1-1-1V6a1 1 0 0 1 1-1zm9 7 8-5H4z"/></svg>
        <span>info@webmail.com</span>
      </div>
      <div class="contact-row web">
        <svg class="contact-icon" viewBox="0 0 24 24" aria-hidden="true" fill="none" stroke="#1c3160" stroke-width="1.8"><circle cx="12" cy="12" r="9"/><ellipse cx="12" cy="12" rx="4" ry="9"/><path d="M3 12h18M5 7h14M5 17h14"/></svg>
        <span>www.website.com</span>
      </div>
      <div class="contact-row address">
        <svg class="contact-icon" viewBox="0 0 24 24" aria-hidden="true"><path d="M12 2a7 7 0 0 0-7 7c0 5.2 7 13 7 13s7-7.8 7-13a7 7 0 0 0-7-7zm0 9.5A2.5 2.5 0 1 1 12 6.5a2.5 2.5 0 0 1 0 5z"/></svg>
        <span>12/C, Address, Street<br>Pincode - 221122</span>
      </div>
    </div>
  </section>

  <section class="card card-back">
    <div class="brand">
      <div class="brand-mark"></div>
      <span class="brand-name">Brookfern</span>
      <span class="brand-sub">Veterinary Hospital</span>
    </div>
  </section>
</body>
</html>
```